Cosmetic injections clinic needs a fresh looking business card

We need a business card using the supplied logo and color scheme to attract future clients to our clinic. It should be modern and fresh, eye catching and not too busy. Simple and to the point is best. I would like two sided designs with the front indicating address and contact information, and the back in full color with white logo and descriptive information also provided.
Target Market(s)
Clients looking for non surgical beauty enhancements.
Contact Information for Business Card
MeloraSkin
14, 618 Birchmont Way
St. Albert, Alberta
K2P 7W3
Phone: 587-412-6630
Email: info@meloraskin.com
Requirements
Must have
- -Logo supplied with the name and address of the clinic
- -Back of card in full color with white logo with A small line of text indicating both of the following: Anti aging consultants and cosmetic injectables
- Located inside the Voyager Wellness Group

```html
<!DOCTYPE html>
<html lang="en">
<head>
<meta charset="utf-8">
<title>MeloraSkin Business Card</title>
<link rel="stylesheet" href="https://fonts.googleapis.com/css2?family=Barlow:wght@500&family=Questrial&family=Raleway:wght@300;700&display=swap">
<style>
  :root {
    --backdrop: #ececec;
    --plum: #6c4699;
    --rose: #e04595;
    --teal: #35b7a2;
    --white: #ffffff;
    --ink: #1d1d1f;
  }
  * { margin: 0; padding: 0; box-sizing: border-box; }
  html, body {
    width: 1200px;
    height: 1200px;
    overflow: hidden;
    background: var(--backdrop);
  }
  .card {
    position: absolute;
    left: 195px;
    width: 845px;
    height: 490px;
    overflow: hidden;
  }
  /* Back side: full colour */
  .card-back {
    top: 79px;
    background: var(--plum);
    color: var(--white);
    text-align: center;
  }
  .brand-lockup {
    position: absolute;
    top: 150px;
    left: 0;
    right: 0;
    display: flex;
    align-items: center;
    justify-content: center;
    gap: 22px;
  }
  .brand-dot {
    width: 74px;
    height: 74px;
    border-radius: 50%;
    background: var(--white);
  }
  .brand-name {
    font-family: "Barlow", sans-serif;
    font-weight: 500;
    font-size: 96px;
    line-height: 1;
    letter-spacing: 1px;
  }
  .card-back .tagline {
    position: absolute;
    top: 375px;
    left: 0;
    right: 0;
    font-family: "Raleway", sans-serif;
    font-weight: 700;
    font-size: 24px;
    letter-spacing: 0.3px;
  }
  .card-back .location {
    position: absolute;
    top: 418px;
    left: 0;
    right: 0;
    font-family: "Raleway", sans-serif;
    font-weight: 300;
    font-size: 22px;
    letter-spacing: 0.3px;
  }
  /* Front side: contact details */
  .card-front {
    top: 631px;
    background: var(--white);
  }
  .card-front .brand-name {
    position: absolute;
    left: 42px;
    top: 52px;
    color: var(--plum);
    font-size: 76px;
  }
  .contact-list {
    position: absolute;
    left: 43px;
    top: 252px;
    list-style: none;
    font-family: "Questrial", sans-serif;
    font-size: 23px;
    color: var(--ink);
    line-height: 29px;
  }
  .contact-item {
    display: flex;
    align-items: flex-start;
    gap: 12px;
    margin-bottom: 11px;
  }
  .contact-icon {
    flex: none;
    width: 32px;
    height: 32px;
    border-radius: 7px;
    background: var(--plum);
    display: flex;
    align-items: center;
    justify-content: center;
  }
  .contact-icon svg { width: 20px; height: 20px; }
  .brand-artwork {
    position: absolute;
    right: 0;
    top: 0;
    width: 425px;
    height: 490px;
    background: linear-gradient(150deg, var(--rose) 0%, #a64597 30%, var(--plum) 58%, #5a8fa0 82%, var(--teal) 100%);
  }
</style>
</head>
<body>

  <section class="card card-back">
    <div class="brand-lockup">
      <span class="brand-dot"></span>
      <span class="brand-name">MeloraSkin</span>
    </div>
    <p class="tagline">Anti aging consultants and cosmetic injectables</p>
    <p class="location">Located inside the Voyager Wellness Group</p>
  </section>

  <section class="card card-front">
    <span class="brand-name">MeloraSkin</span>

    <ul class="contact-list">
      <li class="contact-item">
        <span class="contact-icon">
          <svg viewBox="0 0 20 20" fill="none" stroke="#fff" stroke-width="1.8" stroke-linejoin="round">
            <path d="M3 8c0-2 3-4 7-4s7 2 7 4l-3 1-1-2H7L6 9z" fill="#fff"/>
            <rect x="5" y="10" width="10" height="6" rx="1" fill="#fff"/>
          </svg>
        </span>
        <span>587-412-6630</span>
      </li>
      <li class="contact-item">
        <span class="contact-icon">
          <svg viewBox="0 0 20 20" fill="none" stroke="#fff" stroke-width="1.6" stroke-linejoin="round">
            <rect x="2.5" y="5" width="15" height="10.5" rx="1"/>
            <path d="M2.5 5.5 10 11l7.5-5.5M2.5 15l5.5-5M17.5 15 12 10"/>
          </svg>
        </span>
        <span>info@meloraskin.com</span>
      </li>
      <li class="contact-item">
        <span class="contact-icon">
          <svg viewBox="0 0 20 20" fill="none" stroke="#fff" stroke-width="2" stroke-linejoin="round">
            <path d="M2.5 10 10 3.5l7.5 6.5"/>
            <path d="M5 9v7.5h3.5v-4h3v4H15V9"/>
          </svg>
        </span>
        <span>MeloraSkin<br>14, 618 Birchmont Way<br>St. Albert, Alberta<br>K2P 7W3</span>
      </li>
    </ul>

    <div class="brand-artwork" role="img" aria-label="Brand artwork in plum, rose and teal"></div>
  </section>

</body>
</html>
```